Facebook cover photo and Icon- Pet Related

I am looking to have a few custom cover photos designed for my business Facebook page so I can rotate between them every month.

We are a start up pet product delivery service for our local market. We specialize in dog and cat food and treats.

We want our Facebook page to have the same feel as our website to solidify our brand. Our work in progress website is www.hollowbarnrunners.com. Please not this is still a work in progress and some of the photos may be changing.

Each cover photo have a different look and feel however should still relate to our brand.

We would like 3 cover photos created with a 'theme' around each of the following phrases. Each saying should also be included on the photo itself.

1. You can't buy happiness, but you can buy local and that's kind of the same thing.
3. Sit. Stay. Let us fetch!
4. Making your life easier, theirs healthier and happier.

We are open to dog, cat, and people 'stock' photos being included as long as the photo goes with the saying.

In addition to the cover photos we would like a design for our 'profile photo' as well.

I am including our logos for you to use as needed.

Industry/Entity Type

Delivery Service

Requirements
Must have
• We would like the text over a photo of people with cats and dogs.
Nice to have
• If there is no photos of humans with cats and dogs the next best thing would be a graphic that goes with the text.
Should not have
• Not interested in designs with animated animals.

```html
<!DOCTYPE html>
<html lang="en">
<head>
<meta charset="utf-8">
<title>Hollow Barn Runners – Cover</title>
<link href="https://fonts.googleapis.com/css2?family=Cabin+Sketch:wght@700&family=Roboto:wght@900&display=swap" rel="stylesheet">
<style>
  :root {
    --teal: #2b7c97;
    --teal-deep: #1f6580;
    --teal-light: #3389a3;
    --chalk: #eef3f2;
    --white: #ffffff;
    --tan: #efd99b;
    --tan-deep: #dcc27d;
  }
  html, body {
    margin: 0;
    padding: 0;
    overflow: hidden;
    background: var(--teal-deep);
  }
  .cover {
    position: relative;
    width: 1200px;
    height: 450px;
    overflow: hidden;
    background:
      radial-gradient(ellipse at 45% 45%, var(--teal-light) 0%, var(--teal) 55%, var(--teal-deep) 100%);
  }
  .quote {
    position: absolute;
    left: 60px;
    top: 164px;
    width: 786px;
    margin: 0;
    font-family: "Cabin Sketch", "Trebuchet MS", sans-serif;
    font-weight: 700;
    font-size: 38px;
    line-height: 48px;
    letter-spacing: 2px;
    word-spacing: 4px;
    color: var(--chalk);
    text-align: center;
    white-space: nowrap;
  }
  .quote-mark {
    position: absolute;
    width: 58px;
    height: 40px;
    fill: var(--white);
  }
  .quote-mark--open { left: 90px; top: 149px; }
  .quote-mark--close { left: 752px; top: 284px; }
  .mascot-area {
    position: absolute;
    left: 835px;
    top: 0;
    width: 350px;
    height: 340px;
  }
  .site-url {
    position: absolute;
    right: 22px;
    bottom: 14px;
    margin: 0;
    font-family: "Roboto", Arial, sans-serif;
    font-weight: 900;
    font-size: 19px;
    color: var(--white);
    letter-spacing: 0.3px;
  }
</style>
</head>
<body>
  <main class="cover">
    <svg class="quote-mark quote-mark--open" viewBox="0 0 58 40" aria-hidden="true">
      <g transform="rotate(180 29 20)">
        <circle cx="13" cy="12" r="11"/>
        <path d="M23 13 C23 26 15 34 4 38 L2 34 C9 31 13 26 13 21 Z"/>
        <circle cx="43" cy="12" r="11"/>
        <path d="M53 13 C53 26 45 34 34 38 L32 34 C39 31 43 26 43 21 Z"/>
      </g>
    </svg>
    <p class="quote">You cant buy happiness<br>but you can buy local and thats<br>kind of the same thing.</p>
    <svg class="quote-mark quote-mark--close" viewBox="0 0 58 40" aria-hidden="true">
      <circle cx="13" cy="12" r="11"/>
      <path d="M23 13 C23 26 15 34 4 38 L2 34 C9 31 13 26 13 21 Z"/>
      <circle cx="43" cy="12" r="11"/>
      <path d="M53 13 C53 26 45 34 34 38 L32 34 C39 31 43 26 43 21 Z"/>
    </svg>

    <svg class="mascot-area" viewBox="0 0 350 340" role="img" aria-label="Cartoon dog mascot illustration with a red studded collar">
      <defs>
        <linearGradient id="mascotTone" x1="0" y1="0" x2="0" y2="1">
          <stop offset="0" stop-color="var(--tan)"/>
          <stop offset="1" stop-color="var(--tan-deep)"/>
        </linearGradient>
      </defs>
      <rect x="10" y="10" width="330" height="325" rx="90" fill="url(#mascotTone)" opacity="0.9"/>
    </svg>

    <p class="site-url">www.hollowbarnrunners.com</p>
  </main>
</body>
</html>
```